Postcard Design

We are an upscale, full service real estate boutique based in Mt. Pleasant, SC. We will be having a Grand Opening of our beautiful, new office complete with high end custom home architecture and design. I will attach photos for your review. I would like to come up with a medium postcard to be mailed to clientele of Mt. Pleasant. Home prices between $300,000 - $2.2 million. The customers can call our office for the Grand Opening Listing Promotion or stop by our grand opening. We will have drawings for door prizes that include services at Brambleton Day Spa, Copper Kettle gift certificates, and they can register to win a cruise with a listing presentation. Our Grand Opening will be a couple of different dates, April 7, 2016 and April 21, 2016. I will want an order that lists the 7th and another order that will list the 21. The look should have a very "relaxing, beach" feel, but not Myrtle Beach...should reflect colors of the ocean, like you are on vacation. I will include logos and pics for your review. Thank you!

```html
<!DOCTYPE html>
<html lang="en">
<head>
<meta charset="utf-8">
<title>Seabright Real Estate – Grand Opening Postcard</title>
<link rel="stylesheet" href="https://fonts.googleapis.com/css2?family=Arvo:wght@700&family=Lato:wght@400;700&family=Michroma&display=swap">
<style>
  :root {
    --backdrop: #8a5a2e;
    --paper: #ffffff;
    --ocean: #1f7cc1;
    --ocean-deep: #0f6fb7;
    --sky: #36a9e1;
    --ink: #231f20;
    --stamp: #808080;
    --photo-house-a: #9cc3e2;
    --photo-house-b: #6f8a5a;
    --photo-garden-a: #8fb34c;
    --photo-garden-b: #c56a4a;
    --photo-beach-a: #9fd0ec;
    --photo-beach-b: #e3cfae;
  }
  * { margin: 0; padding: 0; box-sizing: border-box; }
  html, body { width: 907px; height: 1200px; overflow: hidden; }
  body { background: var(--backdrop); position: relative; font-family: "Lato", sans-serif; }

  .postcard { position: absolute; left: 104px; width: 697px; background: var(--paper); overflow: hidden; }
  .postcard--back { top: 42px; height: 541px; }
  .postcard--front { top: 603px; height: 542px; }
  .postcard svg.shapes { position: absolute; inset: 0; }

  .stamp-box { position: absolute; left: 618px; top: 12px; width: 61px; height: 75px; background: var(--stamp); }

  .services-tag {
    position: absolute; left: 66px; top: 207px; width: 160px; height: 36px;
    background: var(--ink); border-radius: 0 0 12px 12px;
    color: #fff; font-weight: 700; font-size: 20px; text-align: center; line-height: 36px;
  }
  .brand-mark-small {
    position: absolute; left: 262px; top: 218px; width: 90px;
    color: #fff; font-weight: 700; font-size: 13px; line-height: 1.15; text-align: center; letter-spacing: 0.5px;
  }
  .services-list { position: absolute; left: 34px; top: 264px; width: 260px; list-style: none; color: #fff; font-size: 13.5px; }
  .services-list li { position: relative; padding-left: 11px; margin-bottom: 7px; line-height: 17px; }
  .services-list li::before { content: "•"; position: absolute; left: 0; }

  .contact-band { position: absolute; left: 22px; top: 371px; color: #fff; font-size: 14px; }
  .contact-band .tagline { font-weight: 700; }
  .contact-item { position: absolute; top: 18px; white-space: nowrap; line-height: 18px; }
  .contact-item .label { color: var(--sky); display: block; }
  .contact-item--phone { left: 0; }
  .contact-item--web { left: 151px; top: 16px; }

  .headline { position: absolute; top: 20px; width: 100%; text-align: center; font-family: "Arvo", serif; font-weight: 700; font-size: 58px; color: var(--ocean); line-height: 70px; }
  .date-band { position: absolute; top: 101px; left: 0; width: 100%; height: 40px; background: var(--ink); color: #fff; text-align: center; font-family: "Michroma", sans-serif; font-size: 23px; line-height: 40px; }
  .price-range { position: absolute; top: 154px; width: 100%; padding-left: 10px; text-align: center; font-family: "Arvo", serif; font-weight: 700; font-size: 25px; color: var(--ink); }
  .brand-mark-large {
    position: absolute; left: 236px; top: 370px; width: 200px; text-align: center;
    font-family: "Lato", sans-serif; font-weight: 700; font-size: 26px; line-height: 1.15; color: var(--ocean); letter-spacing: 2px;
  }
</style>
</head>
<body>

<section class="postcard postcard--back" aria-label="Postcard mailing side">
  <svg class="shapes" width="697" height="541" viewBox="0 0 697 541">
    <defs>
      <linearGradient id="houseTone" x1="0" y1="0" x2="0" y2="1">
        <stop offset="0" stop-color="var(--photo-house-a)"/>
        <stop offset="1" stop-color="var(--photo-house-b)"/>
      </linearGradient>
    </defs>
    <path class="panel-edge" d="M352 0 C385 130 384 300 372 446" fill="none" stroke="var(--sky)" stroke-width="4"/>
    <path class="services-panel" d="M0 0 H344 C376 130 374 300 364 446 H0 Z" fill="var(--ocean)"/>
    <rect class="contact-panel" x="0" y="363" width="366" height="83" fill="var(--ink)"/>
    <path class="photo-edge" d="M0 188 C150 210 300 150 344 0" fill="none" stroke="var(--sky)" stroke-width="12"/>
    <path class="photo-edge" d="M0 188 C150 210 300 150 344 0" fill="none" stroke="var(--paper)" stroke-width="5"/>
    <path role="img" aria-label="Photo of a two-storey blue clapboard house among trees" d="M0 0 H338 C295 140 150 200 0 184 Z" fill="url(#houseTone)"/>
  </svg>
  <div class="stamp-box" aria-hidden="true"></div>
  <div class="services-tag">Services</div>
  <div class="brand-mark-small">Seabright<br>Real Estate</div>
  <ul class="services-list">
    <li>Brambleton Day Spa</li>
    <li>Copper Kettle gift certificates</li>
    <li>They can register to win a cruise with a listing presentation</li>
  </ul>
  <div class="contact-band">
    <p class="tagline">Lorem ipsum dolor sit amet</p>
    <p class="contact-item contact-item--phone"><span class="label">Call</span>0123456789</p>
    <p class="contact-item contact-item--web"><span class="label">Visit us</span>www.companywebsite</p>
  </div>
</section>

<section class="postcard postcard--front" aria-label="Postcard front">
  <svg class="shapes" width="697" height="542" viewBox="0 0 697 542">
    <defs>
      <linearGradient id="gardenTone" x1="0" y1="0" x2="1" y2="1">
        <stop offset="0" stop-color="var(--photo-garden-a)"/>
        <stop offset="1" stop-color="var(--photo-garden-b)"/>
      </linearGradient>
      <linearGradient id="beachTone" x1="0" y1="0" x2="0" y2="1">
        <stop offset="0" stop-color="var(--photo-beach-a)"/>
        <stop offset="1" stop-color="var(--photo-beach-b)"/>
      </linearGradient>
    </defs>
    <path role="img" aria-label="Photo of a couple sitting together on a park bench in a garden" d="M0 182 C150 170 255 230 300 360 L300 542 H0 Z" fill="url(#gardenTone)"/>
    <path role="img" aria-label="Photo of a family sitting together on a sunny beach" d="M697 198 C530 195 430 240 390 340 L380 542 H697 Z" fill="url(#beachTone)"/>
    <path d="M0 165 C160 150 270 215 312 340" fill="none" stroke="var(--ocean-deep)" stroke-width="7"/>
    <path d="M0 176 C155 162 260 222 302 345" fill="none" stroke="var(--sky)" stroke-width="4"/>
    <path d="M697 178 C520 176 420 225 374 340" fill="none" stroke="var(--ocean-deep)" stroke-width="7"/>
    <path d="M697 190 C525 188 428 235 385 345" fill="none" stroke="var(--sky)" stroke-width="4"/>
    <circle cx="336" cy="415" r="122" fill="var(--paper)"/>
    <circle cx="336" cy="415" r="112" fill="none" stroke="var(--ocean-deep)" stroke-width="6"/>
    <circle cx="336" cy="415" r="103" fill="none" stroke="var(--sky)" stroke-width="3"/>
    <rect x="290" y="520" width="92" height="22" fill="var(--paper)"/>
  </svg>
  <h1 class="headline">Grand Opening</h1>
  <p class="date-band">7th AND 21st APRIL, 2016</p>
  <p class="price-range">$300,000 - $2.2 million</p>
  <p class="brand-mark-large">SEABRIGHT<br>REAL ESTATE</p>
</section>

</body>
</html>
```